Flyer Design Project

Business is Wexford In Home Care

We are an Australian provider of In Home Care services.

We have a focus on quality care and a high standard of service.

We are non medical

We want to promote the health, happiness and independence of senior citizens by providing some help at home for general domestic duties (cleaning, bed linnen), personal care (showering, grooming) and meal preparation etc.

Target Market(s)

Seniors (70+) and the Children of seniors.

Industry/Entity Type

Business

Requirements
Must have
• Colour scheme from our website (www.wexfordinhomecare.com.au) –

The uploaded Word doc contains the desired copy.

Leaflet will be a standard A4 size foldout with 6 panels, 3 on each side.

```html
<!DOCTYPE html>
<html lang="en">
<head>
<meta charset="utf-8">
<title>Wexford In Home Care – Flyer</title>
<link rel="stylesheet" href="https://fonts.googleapis.com/css2?family=Courgette&family=Ubuntu:wght@400;500&display=swap">
<style>
  :root {
    --sky-band: #d9e6f5;
    --paper: #eef4fb;
    --navy: #1f3a6e;
    --ink: #222831;
    --orange: #f4a424;
    --divider: #c9d9ec;
    --photo-warm: #e9d8c6;
    --photo-cool: #c9d3dd;
    --white: #ffffff;
  }
  * { margin: 0; padding: 0; box-sizing: border-box; }
  html, body { width: 1200px; height: 848px; overflow: hidden; background: var(--white); }
  .flyer {
    position: relative;
    width: 1200px;
    height: 848px;
    background: var(--paper);
    font-family: "Ubuntu", Arial, sans-serif;
    color: var(--ink);
    overflow: hidden;
  }
  .panel-divider { position: absolute; top: 0; width: 1px; height: 820px; background: var(--divider); }
  .photo { position: absolute; }
  .photo--carer-left {
    left: 0; top: 150px; width: 400px; height: 300px;
    background: linear-gradient(120deg, #f1e2d2 0%, var(--photo-warm) 45%, #d8dde6 100%);
  }
  .photo--carer-right {
    left: 800px; top: 150px; width: 400px; height: 212px;
    background: linear-gradient(110deg, #ecd9c6 0%, #f3ece4 50%, var(--photo-cool) 100%);
  }
  .photo--flower-hands {
    left: 470px; top: 416px; width: 217px; height: 194px;
    background: radial-gradient(circle at 50% 45%, #c2386e 0%, #8a4a3c 28%, #241c1a 60%, #0d0d0d 100%);
    box-shadow: 4px 5px 8px rgba(0,0,0,0.45);
  }
  .header-band { position: absolute; left: 0; top: 0; width: 1200px; height: 240px; }
  .script {
    position: absolute;
    font-family: "Courgette", "Brush Script MT", cursive;
    font-size: 31px;
    color: var(--ink);
    white-space: nowrap;
    line-height: 1;
  }
  .brand {
    position: absolute; left: 815px; top: 56px;
    display: flex; align-items: center; gap: 14px;
  }
  .brand__mark { width: 52px; height: 52px; border-radius: 50%; background: var(--navy); }
  .brand__name { font-size: 25px; color: var(--navy); font-weight: 400; white-space: nowrap; }
  .brand__tagline {
    position: absolute; left: 1088px; top: 92px;
    font-size: 16px; color: var(--orange); white-space: nowrap;
  }
  .services-heading {
    position: absolute; left: 11px; top: 472px;
    font-size: 31px; font-weight: 400; color: var(--ink);
  }
  .services-list {
    position: absolute; left: 11px; top: 524px; width: 380px;
    list-style: none; font-size: 14.5px; line-height: 17.5px;
  }
  .services-list li { position: relative; padding-left: 32px; }
  .services-list li::before { content: "•"; position: absolute; left: 0; }
  .summary-block { position: absolute; left: 484px; top: 240px; font-size: 16px; line-height: 20.6px; }
  .summary-list { list-style: none; }
  .summary-list li { position: relative; padding-left: 51px; }
  .summary-list li::before { content: "•"; position: absolute; left: 5px; }
  .contact {
    position: absolute; left: 416px; top: 630px; width: 400px;
    text-align: center; font-size: 16.5px; line-height: 21px;
  }
  .contact__dot { display: block; width: 28px; height: 28px; margin: 6px auto 10px; border-radius: 50%; background: var(--navy); }
  .contact__gap { height: 19px; }
  .promise {
    position: absolute; left: 800px; top: 405px; width: 400px;
    text-align: center; font-size: 27px; line-height: 43px; color: var(--ink);
  }
  .footer-rule { position: absolute; left: 0; width: 1200px; background: var(--orange); }
  .footer-rule--thin { top: 821px; height: 4px; }
  .footer-rule--thick { top: 834px; height: 8px; }
  .footer-dot {
    position: absolute; left: 327px; top: 782px;
    width: 54px; height: 54px; border-radius: 50%; background: var(--navy);
  }
</style>
</head>
<body>
<main class="flyer">
  <div class="photo photo--carer-left" role="img" aria-label="Photo of a smiling carer with an elderly man"></div>
  <div class="photo photo--carer-right" role="img" aria-label="Photo of a carer embracing a smiling elderly woman"></div>

  <svg class="header-band" viewBox="0 0 1200 240" aria-hidden="true">
    <path d="M0 0 H1200 V166 C1090,150 960,146 860,172 C760,198 640,222 520,214 C420,206 350,180 300,160 C220,135 110,148 0,205 Z" fill="var(--sky-band)"/>
  </svg>

  <div class="panel-divider" style="left:400px"></div>
  <div class="panel-divider" style="left:800px"></div>

  <p class="script" style="left:17px;top:14px">Reliable,</p>
  <p class="script" style="left:50px;top:50px">compassionate,</p>
  <p class="script" style="left:108px;top:88px">person centred...</p>

  <p class="script" style="left:466px;top:22px">Providing</p>
  <p class="script" style="left:506px;top:57px">Exceptional</p>
  <p class="script" style="left:549px;top:96px">Care</p>
  <p class="script" style="left:606px;top:126px">...at home</p>

  <div class="brand">
    <span class="brand__mark"></span>
    <span class="brand__name">Wexford In Home Care</span>
  </div>
  <p class="brand__tagline">a better way</p>

  <h2 class="services-heading">Our services –</h2>
  <ul class="services-list">
    <li>Personal care- showering, dressing, hygiene and grooming</li>
    <li>Domestic Assistance- general cleaning, laundry, bed linen and ironing</li>
    <li>Meal Preparation- support to select, prepare and enjoy meals</li>
    <li>Respite- support for carers to take a well-earned break</li>
    <li>Companionship- visits, social outings, transport to appointments and support shopping</li>
    <li>Rehabilitation- support after surgery or recovering from illness</li>
  </ul>

  <div class="summary-block">
    <p>Our Services</p>
    <ul class="summary-list">
      <li>Personal Care</li>
      <li>Domestic Assistance</li>
      <li>Meal Preparation</li>
      <li>Respite</li>
      <li>Companionship</li>
      <li>Rehabilitation Support</li>
    </ul>
  </div>

  <div class="photo photo--flower-hands" role="img" aria-label="Photo of cupped hands holding a pink flower"></div>

  <div class="contact">
    <p>CALL 1300 555 014</p>
    <span class="contact__dot"></span>
    <p>E: hello@wexfordinhomecare.com.au</p>
    <p>W: wexfordinhomecare.com.au</p>
    <div class="contact__gap"></div>
    <p>Address: Suite 7/215 Harbour Lane</p>
    <p>Sydney NSW 2010</p>
  </div>

  <p class="promise">In-home<br>care specialists<br>offering professional,<br>non-medical,<br>companion based care<br>in the comfort and<br>familiarity<br>of your home.</p>

  <div class="footer-rule footer-rule--thin"></div>
  <div class="footer-rule footer-rule--thick"></div>
  <div class="footer-dot"></div>
</main>
</body>
</html>
```